Flyer Advertisement Design for exotic rental company

Design an advertisement for a exotic rental company:

https://zoomvela.com/

Here is a similar business:

https://www.gildmarquerides.com/

I rent out a vehicle called a Tundrix Whipcraft. Here is a link to the manufacturer website:

https://whipcraft.tundrix.com/en-us/

I have the 2018 Tundrix Whipcraft GT in the colors Navy Blue and Sunset Red

This advertisement will be printed on a flyer and placed in strategic locations to attract customers. I am looking for something that will draw the customer in. Please use your imagination and come up with something awesome!

Target Market(s)

Outgoing individuals looking to have some fun! This advertisement will be placed in a country club

Industry/Entity Type

Rental Car

Font styles to use
Serif
Sans Serif
Decorative
Script

Colors

Designer to choose colors to be used in the design.

Requirements
Must have
• Pictures of the Tundrix Whipcraft, website info, message about discount to Hollowbrook Country Club Members, phone number, anything else you feel will make the advertisement look great
Nice to have
• Anything you suggest in your professional capacity
Should not have
• Anything goes!

```html
<!DOCTYPE html>
<html lang="en">
<head>
<meta charset="utf-8">
<title>Rent Me – Zoomvela Flyer</title>
<link rel="stylesheet" href="https://fonts.googleapis.com/css2?family=Russo+One&family=Montserrat:ital,wght@1,500;1,700;1,800;1,900&display=swap">
<style>
  :root {
    --page-bg: #d9d9d9;
    --night: #02040c;
    --navy: #0a1f6b;
    --royal: #1646c8;
    --bright-blue: #2f7fe0;
    --sky-top: #1c4f9e;
    --sky-low: #3a5c8c;
    --water: #2a4258;
    --silver-light: #ffffff;
    --silver-mid: #c9ccd2;
    --silver-dark: #7d828c;
    --white: #ffffff;
  }
  * { box-sizing: border-box; margin: 0; padding: 0; }
  html, body { width: 1200px; height: 900px; overflow: hidden; }
  body { background: var(--page-bg); position: relative; font-family: "Montserrat", sans-serif; }

  .flyer {
    position: absolute; left: 268px; top: 20px;
    width: 664px; height: 860px; overflow: hidden;
    background: linear-gradient(180deg, var(--night) 50%, #050c2a 80%, #071a5a 100%);
  }
  .backdrop { position: absolute; inset: 0; width: 100%; height: 100%; }

  .headline {
    position: absolute; top: 40px; left: 0; width: 100%;
    text-align: center; font-family: "Russo One", sans-serif;
    font-size: 104px; line-height: 1; letter-spacing: -2px;
    transform: skewX(-14deg) scaleX(1.12);
    background: linear-gradient(180deg, var(--silver-light) 20%, var(--silver-mid) 50%, var(--silver-dark) 56%, var(--silver-light) 90%);
    -webkit-background-clip: text; background-clip: text; color: transparent;
    filter: drop-shadow(2px 3px 2px rgba(0,0,0,.7));
  }
  .site-bar {
    position: absolute; top: 148px; left: 40px; width: 590px; height: 36px;
    background: linear-gradient(90deg, rgba(22,70,200,0) 0%, var(--royal) 20%, var(--royal) 80%, rgba(22,70,200,0) 100%);
    display: flex; align-items: center; justify-content: center;
  }
  .site-bar__text {
    color: var(--white); font-style: italic; font-weight: 500;
    font-size: 27px; letter-spacing: 0.42em; white-space: nowrap;
    text-shadow: 1px 2px 2px rgba(0,0,0,.6);
  }
  .vehicle {
    position: absolute; left: 85px; top: 196px; width: 505px; height: 295px;
    border-radius: 40% 30% 20% 20%;
    background: radial-gradient(ellipse at 45% 55%, #1a2f78 0%, #0c1848 45%, #05081a 75%, rgba(5,8,26,0) 100%);
  }
  .phone {
    position: absolute; top: 506px; left: 0; width: 100%; text-align: center;
    font-family: "Russo One", sans-serif; font-size: 66px; line-height: 1;
    transform: skewX(-14deg);
    background: linear-gradient(180deg, var(--silver-light) 20%, var(--silver-mid) 50%, var(--silver-dark) 56%, var(--silver-light) 92%);
    -webkit-background-clip: text; background-clip: text; color: transparent;
  }
  .offer {
    position: absolute; top: 584px; left: 0; width: 100%; text-align: center;
    color: var(--white); font-style: italic; font-weight: 500;
    font-size: 25px; line-height: 1.3;
  }
  .offer strong { font-weight: 800; }
  .signup-band {
    position: absolute; top: 712px; left: 60px; width: 560px; height: 50px;
    background: linear-gradient(90deg, rgba(22,70,200,0) 0%, var(--royal) 25%, var(--bright-blue) 50%, var(--royal) 75%, rgba(22,70,200,0) 100%);
    display: flex; align-items: center; justify-content: center;
  }
  .signup-band__text {
    color: var(--white); font-style: italic; font-weight: 900;
    font-size: 44px; letter-spacing: -2px; text-transform: uppercase;
    text-shadow: 2px 2px 2px rgba(0,0,0,.5);
  }
  .signup-url {
    position: absolute; top: 766px; left: 0; width: 100%; text-align: center;
    color: var(--white); font-style: italic; font-weight: 500; font-size: 25px;
  }
</style>
</head>
<body>
  <main class="flyer">
    <svg class="backdrop" viewBox="0 0 664 860" preserveAspectRatio="none" aria-hidden="true">
      <defs>
        <linearGradient id="skyline" x1="0" y1="0" x2="0" y2="1">
          <stop offset="0" stop-color="#1c4f9e"/>
          <stop offset="0.5" stop-color="#3a5c8c"/>
          <stop offset="0.62" stop-color="#6a5a70"/>
          <stop offset="0.7" stop-color="#2a4258"/>
          <stop offset="1" stop-color="#1d2f44"/>
        </linearGradient>
        <linearGradient id="streak" x1="0" y1="0" x2="1" y2="0">
          <stop offset="0" stop-color="#1646c8" stop-opacity="0.9"/>
          <stop offset="0.6" stop-color="#2f7fe0"/>
          <stop offset="1" stop-color="#1646c8" stop-opacity="0.6"/>
        </linearGradient>
      </defs>
      <polygon points="0,0 664,0 664,520 0,400" fill="url(#streak)"/>
      <polygon role="img" aria-label="Night city skyline over a waterfront" points="0,0 664,0 664,470 0,345" fill="url(#skyline)"/>
      <polygon points="180,490 664,545 664,565 300,525" fill="#2f9fe8" opacity="0.8"/>
      <polygon points="560,560 664,600 664,670 600,600" fill="#1646c8" opacity="0.7"/>
    </svg>

    <h1 class="headline">RENT ME</h1>
    <div class="site-bar"><span class="site-bar__text">WWW.ZOOMVELA.COM</span></div>

    <div class="vehicle" role="img" aria-label="Navy blue Tundrix Whipcraft GT three-wheel roadster"></div>

    <p class="phone">555 274 8160</p>
    <p class="offer"><strong>20%</strong> Off for all Hollowbrook Country<br>Club Members</p>

    <div class="signup-band"><span class="signup-band__text">Sign up at</span></div>
    <p class="signup-url">www.zoomvela.com/HollowbrookCC</p>
  </main>
</body>
</html>
```